Offshore Energy Projects Management Consultancy needs a business card design

Logo available. We provide teams to deliver engineering consultancy, project management and delivery teams mainly in the offshore renewables sector. The company is all about bringing the right people to a project to deliver the scope.

The business card will be used for all staff.

The business card should be quite simple, vibrant and uncluttered but convey experience, enthusiasm and integration.

Target Market(s)

Energy Project Developers and Tier 1 construction companies

Contact Information for Business Card

Logo should be on the back of the card. I'm happy for the designer to play with the colour of the logo and background colour.

Front of the card should convey all the must have information in a clear and professional manner but without being overly traditional.

Colors

Designer to choose colors to be used in the design.

Requirements
Must have
• Land Line Tel Number, Mobile Tel Number, Email, business address, web address.

```html
<!DOCTYPE html>
<html lang="en">
<head>
<meta charset="utf-8">
<title>Tidewater Project Partners – Business Card</title>
<link rel="stylesheet" href="https://fonts.googleapis.com/css2?family=Roboto:wght@400;500;700&display=swap">
<style>
  :root {
    --backdrop: #505151;
    --brand-blue: #0f77be;
    --accent-blue: #22a7e0;
    --white: #ffffff;
  }
  * { margin: 0; padding: 0; box-sizing: border-box; }
  html, body {
    width: 963px; height: 1200px; overflow: hidden;
    background: var(--backdrop);
    font-family: "Roboto", Arial, sans-serif;
  }
  .card {
    position: absolute; left: 231px;
    width: 559px; height: 319px;
    background: var(--brand-blue);
    color: var(--white);
    overflow: hidden;
  }
  .card--front { top: 221px; }
  .card--back { top: 634px; }

  .front-circle { position: absolute; left: 0; top: 0; }

  .contact { position: absolute; left: 25px; top: 76px; }
  .contact__name { font-size: 18px; font-weight: 700; line-height: 1.2; }
  .contact__title { font-size: 12.5px; font-weight: 500; margin-top: 2px; }
  .contact__address { font-size: 12.5px; line-height: 16px; margin-top: 18px; }
  .contact__list { list-style: none; margin-top: 8px; font-size: 12.5px; }
  .contact__list li { display: flex; align-items: center; height: 16px; }
  .contact__list svg { width: 10px; height: 10px; margin-right: 8px; fill: var(--white); flex: none; }

  .brand-front {
    position: absolute; left: 260px; width: 270px; top: 130px;
    text-align: center;
    color: var(--brand-blue);
    font-size: 19px; font-weight: 700; line-height: 1.25;
  }
  .brand-back {
    position: absolute; left: 0; right: 0; top: 128px;
    text-align: center; font-size: 32px; font-weight: 700;
  }
  .back-web {
    position: absolute; left: 0; right: 0; top: 272px;
    text-align: center; font-size: 13px;
  }
</style>
</head>
<body>
  <section class="card card--front">
    <svg class="front-circle" width="559" height="319" viewBox="0 0 559 319">
      <circle cx="382" cy="160" r="162" fill="var(--accent-blue)"/>
      <circle cx="382" cy="160" r="160" fill="var(--white)"/>
      <circle cx="382" cy="160" r="158" fill="var(--accent-blue)"/>
      <circle cx="382" cy="160" r="155" fill="var(--white)"/>
    </svg>

    <div class="contact">
      <div class="contact__name">Daniel Hart</div>
      <div class="contact__title">President</div>
      <div class="contact__address">2140 Harbor View Road<br>Seaford, Maine 04912</div>
      <ul class="contact__list">
        <li><svg viewBox="0 0 10 10"><path d="M2 0.5l1.6 2-1 1.2c.6 1.3 1.4 2.1 2.7 2.7l1.2-1 2 1.6-1 1.9C4 8.6 1.4 6 0.5 1.5z"/></svg>555-214-9836</li>
        <li><svg viewBox="0 0 10 10"><path d="M2.5 0h5v10h-5zM3.5 1v7h3V1z"/></svg>555-418-2673</li>
        <li><svg viewBox="0 0 10 10"><path d="M0 2h10v1L5 6 0 3zM0 4l5 3 5-3v4H0z"/></svg>hello@tidewaterpartners.com</li>
        <li><svg viewBox="0 0 10 10"><circle cx="5" cy="5" r="5"/></svg>www.tidewaterpartners.com</li>
      </ul>
    </div>

    <div class="brand-front">Tidewater<br>Project Partners</div>
  </section>

  <section class="card card--back">
    <div class="brand-back">Tidewater Project Partners</div>
    <div class="back-web">www.tidewaterpartners.com</div>
  </section>
</body>
</html>
```